Design eines Praxisschilds für Hausarztpraxis
Zielgruppe
Hausarztpraxis, Zielgruppe sind die Bewohner vor Ort, bodenständig
Aufgabenstellung
Praxisschild entwerfen, es soll schlicht sein. Das angefügte Logo bitte verwenden, ggf. auch nur das Symbol ohne Namen verwenden und den Namen extra in schwarz aufführen.
Farben:
- schwarz
- Pantone 13-0645 Limeade
- Pantone 7726
Text:
Dr. med. Jonas Walbrecht
Facharzt für Innere Medizin
Facharzt für Allgemeinmedizin
Sprechzeiten:
Montag bis Freitag 07:30 – 12:00 Uhr
Dienstag und Donnerstag 17:00 – 19:00 Uhr
und nach Vereinbarung
Tel: 0761 83172
www.hausarzt-beispielau.de
Format quer (die Maße sind leider vorgegeben): 55,7 cm x 42,8 cm

```html
<!DOCTYPE html>
<html lang="de">
<head>
<meta charset="utf-8">
<title>Praxisschild – Dr. med. Jonas Walbrecht</title>
<link rel="stylesheet" href="https://fonts.googleapis.com/css2?family=Hanken+Grotesk:wght@400;600;700&display=swap">
<style>
  :root {
    --limeade: #d3d75c;
    --praxis-blue: #235a80;
    --muted-grey: #b9b9b9;
    --paper: #ffffff;
  }
  * { margin: 0; padding: 0; box-sizing: border-box; }
  html, body { width: 1200px; height: 922px; overflow: hidden; background: var(--paper); }
  .sign {
    position: relative;
    width: 1200px;
    height: 922px;
    background: var(--paper);
    font-family: "Hanken Grotesk", Arial, sans-serif;
    color: var(--praxis-blue);
  }
  .line {
    position: absolute;
    left: 0;
    width: 100%;
    text-align: center;
    line-height: 1;
    white-space: nowrap;
  }
  .brand-mark {
    position: absolute;
    left: 131px;
    top: 104px;
    width: 158px;
    height: 160px;
    display: flex;
    flex-direction: column;
    align-items: center;
    justify-content: center;
    gap: 10px;
  }
  .brand-mark .dot {
    width: 112px;
    height: 112px;
    border-radius: 50%;
    background: var(--limeade);
  }
  .brand-mark .brand-name {
    font-size: 15px;
    font-weight: 600;
    color: var(--praxis-blue);
    letter-spacing: 0.04em;
  }
  .header { left: 303px; width: 748px; font-weight: 400; letter-spacing: 0.12em; }
  .doctor-name { top: 110px; font-size: 36px; color: var(--limeade); }
  .specialty { font-size: 36px; }
  .specialty.first { top: 165px; }
  .specialty.second { top: 219px; }
  .hours-title {
    top: 350px;
    font-size: 27px;
    font-weight: 700;
    letter-spacing: 0.42em;
    color: var(--limeade);
    padding-left: 0.42em;
  }
  .hours-title .colon { color: var(--muted-grey); }
  .hours { font-size: 40px; font-weight: 600; }
  .hours.weekdays { top: 431px; }
  .hours.evenings { top: 501px; }
  .hours.appointment { top: 571px; }
  .contact { font-weight: 600; }
  .contact.phone { top: 721px; font-size: 29px; }
  .contact.web { top: 767px; font-size: 27px; letter-spacing: 0.01em; }
</style>
</head>
<body>
  <main class="sign">
    <div class="brand-mark">
      <span class="dot"></span>
      <span class="brand-name">Praxis Walbrecht</span>
    </div>

    <p class="line header doctor-name">DR. MED. JONAS WALBRECHT</p>
    <p class="line header specialty first">FACHARZT FÜR INNERE MEDIZIN</p>
    <p class="line header specialty second">FACHARZT FÜR ALLGEMEINMEDIZIN</p>

    <h2 class="line hours-title">SPRECHZEITEN<span class="colon">:</span></h2>

    <p class="line hours weekdays">Montag bis Freitag 07:30 – 12:00 Uhr</p>
    <p class="line hours evenings">Dienstag und Donnerstag 17:00 – 19:00 Uhr</p>
    <p class="line hours appointment">und nach Vereinbarung</p>

    <p class="line contact phone">Tel: 0761 83172</p>
    <p class="line contact web">www.hausarzt-beispielau.de</p>
  </main>
</body>
</html>
```